Email Signature

Our company is having its 10th anniversary in 2021. We would like a new email signature to celebrate the occasion. Attached is our business card design.
Please refer to our website for actual contact details.
www.corvanhold.com.au

Industry/Entity Type

Real Estate

Requirements
Must have
• Our logo
Email
Contact Numbers
Address
Website address

Celebrating 10 years in 2021
Nice to have
• Something that blends the designs of our website and business card

```html
<!DOCTYPE html>
<html lang="en">
<head>
<meta charset="utf-8">
<title>Corvan Group – Email Signature</title>
<link rel="stylesheet" href="https://fonts.googleapis.com/css2?family=Mulish:wght@700&family=Didact+Gothic&display=swap">
<style>
  :root {
    --brand-blue: #1e63ad;
    --ink: #111418;
    --text: #262a30;
    --paper: #ffffff;
    --backdrop: #e6e8eb;
  }
  * { margin: 0; padding: 0; box-sizing: border-box; }
  html, body { width: 1200px; height: 789px; overflow: hidden; background: var(--backdrop); }
  .signature {
    position: absolute; left: 0; top: 140px;
    width: 1200px; height: 508px;
    background: var(--paper);
    font-family: "Didact Gothic", "Century Gothic", sans-serif;
    color: var(--text);
  }
  .person-name {
    position: absolute; left: 50px; top: 88px;
    font-family: "Mulish", sans-serif; font-weight: 700;
    font-size: 40px; color: var(--ink); letter-spacing: 0.3px;
  }
  .person-role { position: absolute; left: 52px; top: 128px; font-size: 29px; }
  .role-rule { position: absolute; left: 50px; top: 175px; width: 109px; height: 6px; background: var(--brand-blue); }
  .company-name {
    position: absolute; right: 46px; top: 214px;
    font-family: "Mulish", sans-serif; font-weight: 700;
    font-size: 48px; letter-spacing: 1px; color: var(--brand-blue);
  }
  .contact-column { position: absolute; top: 304px; font-size: 25px; line-height: 40px; }
  .contact-column li { list-style: none; display: flex; align-items: center; gap: 14px; white-space: nowrap; }
  .contact-column svg { width: 24px; height: 24px; fill: var(--brand-blue); flex: none; }
  .col-phone { left: 58px; }
  .col-web { left: 356px; }
  .col-address { left: 767px; }
  .col-address li { display: block; }
  .web-strong { font-weight: 700; font-family: "Mulish", sans-serif; color: var(--brand-blue); font-size: 24px; }
  .divider { position: absolute; top: 316px; width: 3px; height: 58px; background: var(--brand-blue); }
  .divider-one { left: 299px; }
  .divider-two { left: 729px; }
  .skyline-band {
    position: absolute; left: 0; bottom: 0; width: 1200px; height: 128px;
    background: linear-gradient(to bottom, #2f74bd 0%, var(--brand-blue) 35%);
  }
  .anniversary {
    position: absolute; left: 0; bottom: 10px; width: 1200px;
    text-align: center; color: var(--paper);
    font-size: 25px; letter-spacing: 3.5px;
  }
</style>
</head>
<body>
  <main class="signature">
    <h1 class="person-name">Daniel R, Marlowe</h1>
    <p class="person-role">Owner</p>
    <div class="role-rule"></div>

    <div class="company-name">CORVAN GROUP</div>

    <ul class="contact-column col-phone">
      <li>
        <svg viewBox="0 0 24 24" aria-hidden="true"><path d="M7 1h10a2 2 0 0 1 2 2v18a2 2 0 0 1-2 2H7a2 2 0 0 1-2-2V3a2 2 0 0 1 2-2zm0 3v14h10V4z"/></svg>
        555-014-7102
      </li>
      <li>
        <svg viewBox="0 0 24 24" aria-hidden="true"><path d="M2 8c0-3 5-5 10-5s10 2 10 5v2h-5V8c-1-1-3-1.5-5-1.5S8 7 7 8v2H2zm4 4h12l3 8H3zm6 1.5a2.5 2.5 0 1 0 0 5 2.5 2.5 0 0 0 0-5z"/></svg>
        555-013-1909
      </li>
    </ul>
    <div class="divider divider-one"></div>

    <ul class="contact-column col-web">
      <li>
        <svg viewBox="0 0 24 24" aria-hidden="true"><path d="M2 5h20v14H2zm2 2v.5l8 5.5 8-5.5V7z"/></svg>
        danmarlowe@mailbox.com
      </li>
      <li>
        <svg viewBox="0 0 24 24" aria-hidden="true"><path d="M12 2a10 10 0 1 1 0 20 10 10 0 0 1 0-20zm-1 4c-2 1-4 3-4 5l3 1 1 3 2 1v-3l2-2-1-3h-2z"/></svg>
        <span>www.<span class="web-strong">corvanhold</span>.com</span>
      </li>
    </ul>
    <div class="divider divider-two"></div>

    <ul class="contact-column col-address">
      <li>2240 n. Harbor Avenue #105</li>
      <li>Palm Shore, Florida 33400</li>
    </ul>

    <div class="skyline-band" role="img" aria-label="Blue city skyline silhouette along the bottom edge"></div>
    <p class="anniversary">Celebrating 10 years in 2021</p>
  </main>
</body>
</html>
```